Copper Lantern Fitness Flyer

We need a Flyer designed for a Revolutionary Fresh New Functional Fitness facility in Manly Sydney, Australia. We have just recently opened and now need to get the word out. Using the flyers to hand out at events also for shop counters and letterbox drops.

Our company name is Copper Lantern Fitness "Where STRENGTH Meets Your SPIRIT".
We promote health and fitness to all fitness levels concentrating on functional fitness. To learn more about us and our colour scheme see attached file and also check us out on www.brightpage.example/copperlanternfitnessoz

A5 Size please

Target Market(s)

The beauty of our system is it is for everyone we have girls and guys in there teens, 20's 30's 40's and 50's. Not only that we have professional athletes, military and high fitness levels all the way to people who are overweight and need to loose weight and tone up. The system caters for everyone.

Industry/Entity Type

Fitness

Requirements
Must have
• FRONT:

Free 30min Fat Blasting Experience With Your Very Own Personal Trainer !!!

New Class Starts Every 3 minutes.
30 minute Workout With A Trainer.
No Machines No Mirrors And No Attitudes.
Catering For All Fitness Levels.
Results Guaranteed Or Your Money Back.
Fun, Fresh, Clean, Revolutionary New Facility.

Back:

You Are Just Moments Away From Burning Fat Faster Than Ever Before And Getting That Body You Always Wanted !!!

Come In Today To Claim Your FREE Workout.

Ph (02) 9000 5172
Address 5/117 Kestrel Rd North Manly 2100
www.brightpage.example/copperlanternfitnessoz
Nice to have
• FRONT:

Back:

Ph (02) 9000 5172

```html
<!DOCTYPE html>
<html lang="en">
<head>
<meta charset="utf-8">
<title>Copper Lantern Fitness Flyer</title>
<link rel="stylesheet" href="https://fonts.googleapis.com/css2?family=Abril+Fatface&family=Playfair+Display:wght@700;900&family=Open+Sans:wght@400;700&family=Oswald:wght@300;600&display=swap">
<style>
  :root {
    --backdrop: #1f1f1f;
    --card-dark: #141617;
    --band: #4a4f4f;
    --gold: #b89b4f;
    --gold-light: #d2b66a;
    --green: #7cc242;
    --text-light: #d9d9d9;
    --white: #ffffff;
  }
  * { margin: 0; padding: 0; box-sizing: border-box; }
  html, body { width: 793px; height: 1200px; overflow: hidden; }
  body { background: var(--backdrop); position: relative; font-family: "Open Sans", sans-serif; }

  .flyer { position: absolute; overflow: hidden; box-shadow: 0 4px 14px rgba(0,0,0,.6); }

  /* FRONT */
  .flyer-front { left: 52px; top: 73px; width: 676px; height: 479px;
    background: linear-gradient(180deg, #2a3132 0%, #15191a 60%, #0e1011 100%); }
  .front-photo { position: absolute; left: 0; top: 0; width: 390px; height: 479px;
    background: radial-gradient(ellipse at 45% 55%, #8a5c3d 0%, #5a3a27 35%, #2a2522 70%, rgba(20,24,25,0) 100%); }
  .headline-band { position: absolute; left: 350px; top: 0; width: 326px; height: 196px;
    background: linear-gradient(90deg, rgba(74,79,79,0) 0%, var(--band) 18%, #565b5a 100%); }
  .headline-free { position: absolute; left: 362px; top: 8px; font-family: "Abril Fatface", serif;
    font-size: 124px; line-height: 1; color: var(--gold); letter-spacing: 1px; }
  .headline-offer { position: absolute; left: 364px; top: 124px; width: 310px;
    font-family: "Playfair Display", serif; font-weight: 900; font-size: 17.5px; line-height: 22px; color: var(--gold); }
  .benefits { position: absolute; left: 364px; top: 222px; list-style: none; }
  .benefits li { font-weight: 700; font-size: 12.5px; line-height: 26px; color: var(--text-light); }
  .front-brand { position: absolute; left: 510px; top: 400px; display: flex; align-items: center; gap: 8px; }

  .brand-mark { width: 44px; height: 44px; background: var(--gold); flex: none; }
  .brand-name { font-family: "Open Sans", sans-serif; font-weight: 700; font-size: 13px; line-height: 14px;
    color: var(--gold-light); text-transform: uppercase; }
  .brand-tagline { font-size: 6.5px; color: var(--gold-light); margin-top: 2px; font-weight: 400; text-transform: none; }

  /* BACK */
  .flyer-back { left: 46px; top: 617px; width: 687px; height: 495px; background: var(--card-dark); }
  .back-panel { position: absolute; left: 0; top: 0; width: 238px; height: 495px;
    background: linear-gradient(180deg, #1a1c1d 0%, #0f1011 100%); }
  .back-brand { position: absolute; left: 28px; top: 44px; display: flex; align-items: center; gap: 10px; }
  .back-brand .brand-mark { width: 52px; height: 52px; }
  .back-brand .brand-name { font-size: 15px; line-height: 16px; }
  .cta { position: absolute; left: 34px; top: 172px; color: var(--green); font-family: "Oswald", sans-serif; }
  .cta-lead { font-weight: 300; font-size: 24px; line-height: 32px; text-transform: uppercase; }
  .cta-free { font-weight: 600; font-size: 66px; line-height: 62px; margin-top: 4px; }
  .cta-workout { font-weight: 600; font-size: 34px; line-height: 36px; }
  .cta-body { position: absolute; left: 34px; top: 342px; width: 200px; font-size: 9.5px; line-height: 13px; color: var(--text-light); }
  .social { position: absolute; left: 36px; top: 444px; display: flex; align-items: center; gap: 6px;
    font-weight: 700; font-size: 10px; color: var(--white); }
  .social-mark { width: 36px; height: 36px; background: #3b5d9c; }
  .gold-divider { position: absolute; left: 238px; top: 0; width: 6px; height: 495px; background: var(--gold); }
  .back-photo { position: absolute; left: 244px; top: 0; width: 443px; height: 495px;
    background: linear-gradient(170deg, #e6e8ea 0%, #9c9fa2 18%, #3a3c3e 40%, #2d2f30 65%, #3e6a2e 85%, #4a8a33 100%); }
  .contacts { position: absolute; left: 360px; top: 352px; transform: rotate(-12deg); transform-origin: left top; color: var(--white); }
  .contacts-title { font-family: "Oswald", sans-serif; font-weight: 300; font-size: 34px; line-height: 38px; letter-spacing: 1px; }
  .contacts-phone { font-weight: 700; font-size: 27px; line-height: 34px; }
  .contacts-address { font-size: 11.5px; line-height: 16px; }
</style>
</head>
<body>
  <section class="flyer flyer-front">
    <div class="front-photo" role="img" aria-label="Athletic woman in a black sports top, photographed against a dark background"></div>
    <div class="headline-band"></div>
    <h1 class="headline-free">Free</h1>
    <p class="headline-offer">30min Fat Blasting Experience With Your Very Own Personal Trainer !!!</p>
    <ul class="benefits">
      <li>-New Class Starts Every 3 minutes</li>
      <li>-30 minute Workout With A Trainer</li>
      <li>-No Machines No Mirrors And No Attitudes</li>
      <li>-Catering For All Fitness Levels</li>
      <li>-Results Guaranteed Or Your Money Back</li>
      <li>-Fun, Fresh, Clean, Revolutionary New Facility</li>
    </ul>
    <div class="front-brand">
      <span class="brand-mark"></span>
      <div class="brand-name">Copper<br>Lantern<br>Fitness<div class="brand-tagline">Where Strength Meets Your Spirit</div></div>
    </div>
  </section>

  <section class="flyer flyer-back">
    <div class="back-panel"></div>
    <div class="back-brand">
      <span class="brand-mark"></span>
      <div class="brand-name">Copper<br>Lantern<br>Fitness<div class="brand-tagline">Where Strength Meets Your Spirit</div></div>
    </div>
    <div class="cta">
      <p class="cta-lead">Come in today<br>to claim your</p>
      <p class="cta-free">FREE</p>
      <p class="cta-workout">WORKOUT</p>
    </div>
    <p class="cta-body">You Are Just Moments Away From Burning Fat Faster Than Ever Before And Getting That Body You Always Wanted !!!</p>
    <div class="social"><span class="social-mark"></span>copperlanternfitnessoz</div>
    <div class="gold-divider"></div>
    <div class="back-photo" role="img" aria-label="Functional training floor with hanging punch bags, kettlebells, step platforms, a spin bike, running track and turf strip"></div>
    <div class="contacts">
      <p class="contacts-title">CONTACTS</p>
      <p class="contacts-phone">Ph (02) 9000 5172</p>
      <p class="contacts-address">Shop 5, 117 Kestrel Road Manly, New South Wales</p>
    </div>
  </section>
</body>
</html>
```